i need a business card for a plumbing company in california

we are a drain cleaning , maintenance plumbing company who is starting new marketing campaign for a tatrench-less pipe installation department .

the professional who appreciates time and quality workmanship.

Plumbing

0655a3
ec1f27

• the second logo needs to be included
• a focus on the services offered
• any underlined words on the brief

```html
<!DOCTYPE html>
<html lang="en">
<head>
<meta charset="utf-8">
<title>Clearline Pipeworks – Business Card</title>
<link rel="stylesheet" href="https://fonts.googleapis.com/css2?family=Open+Sans:wght@400;600&family=Titillium+Web:wght@700&display=swap">
<style>
  :root {
    --bg: #e9e8f3;
    --card: #f6f6fa;
    --brand-blue: #0655a3;
    --brand-red: #ec1f27;
    --logo-grey: #6e6e6e;
    --text-blue: #2f5fa8;
    --deco-a: rgba(214, 224, 240, 0.75);
    --deco-b: rgba(236, 214, 196, 0.55);
  }
  * { box-sizing: border-box; margin: 0; padding: 0; }
  html, body { width: 1200px; height: 873px; overflow: hidden; }
  body {
    background: var(--bg);
    font-family: "Open Sans", Arial, sans-serif;
    display: flex;
    flex-direction: column;
    align-items: center;
    justify-content: center;
    gap: 40px;
  }
  .card {
    position: relative;
    width: 640px;
    height: 366px;
    background: var(--card);
    box-shadow: 0 6px 18px rgba(60, 60, 100, 0.15);
    overflow: hidden;
  }
  .card-deco {
    position: absolute;
    border-radius: 50%;
    background: radial-gradient(circle at 40% 60%, var(--deco-b), var(--deco-a) 65%);
  }
  .brand {
    position: absolute;
    display: flex;
    align-items: center;
    gap: 10px;
    font-family: "Titillium Web", Arial, sans-serif;
    font-weight: 700;
    color: var(--logo-grey);
    line-height: 1;
  }
  .brand-dot {
    display: inline-block;
    border-radius: 50%;
    background: var(--brand-red);
  }

  /* Front */
  .card-front .card-deco { width: 270px; height: 270px; left: 200px; top: 40px; }
  .card-front .brand { left: 0; right: 0; top: 140px; justify-content: center; font-size: 40px; }
  .card-front .brand-dot { width: 22px; height: 22px; }
  .services-band {
    position: absolute;
    left: 0; right: 0; bottom: 0;
    height: 30px;
    background: var(--brand-blue);
    color: #fff;
    font-size: 10.5px;
    display: flex;
    align-items: center;
    justify-content: center;
    letter-spacing: 0.1px;
  }

  /* Back */
  .card-back .card-deco { width: 250px; height: 250px; left: 200px; top: 60px; }
  .card-back .brand { right: 26px; top: 24px; font-size: 20px; }
  .card-back .brand-dot { width: 12px; height: 12px; }
  .holder {
    position: absolute;
    left: 0; right: 0; top: 150px;
    text-align: center;
    color: var(--text-blue);
  }
  .holder-name { font-size: 26px; font-weight: 600; }
  .holder-rule {
    width: 150px; height: 3px;
    margin: 6px auto 6px;
    background: var(--brand-red);
  }
  .holder-role { font-size: 14px; }
  .contact {
    position: absolute;
    display: flex;
    align-items: center;
    gap: 6px;
    font-size: 11px;
    color: var(--text-blue);
  }
  .contact svg { width: 11px; height: 11px; flex: none; }
  .contact-social { left: 28px; top: 40px; }
  .contact-video { left: 28px; bottom: 120px; }
  .contact-phone { left: 28px; bottom: 30px; }
  .contact-web {
    right: 28px; bottom: 30px;
    flex-direction: column;
    align-items: flex-end;
    gap: 3px;
  }
</style>
</head>
<body>

  <section class="card card-front">
    <div class="card-deco" role="img" aria-label="Faint decorative illustration of a pipe and buildings"></div>
    <div class="brand"><span>Clearline Pipeworks</span><span class="brand-dot"></span></div>
    <div class="services-band">Virgin Trench-Less Sewer Installs &amp; Replacements – Pipe Bursting &amp; Pipe Pinning Install, Replacement Pipe Enlargement Pull &amp; GO</div>
  </section>

  <section class="card card-back">
    <div class="card-deco" role="img" aria-label="Faint decorative illustration of a pipe and buildings"></div>
    <div class="brand"><span>Clearline Pipeworks</span><span class="brand-dot"></span></div>

    <div class="holder">
      <div class="holder-name">Marco Delgado</div>
      <div class="holder-rule"></div>
      <div class="holder-role">Owner</div>
    </div>

    <div class="contact contact-social">
      <svg viewBox="0 0 10 10"><circle cx="5" cy="5" r="5" fill="var(--brand-blue)"/></svg>
      <span>@ClearlinePipeworks</span>
    </div>
    <div class="contact contact-video">
      <svg viewBox="0 0 10 10"><circle cx="5" cy="5" r="5" fill="var(--brand-red)"/></svg>
      <span>ClearlinePipeworks</span>
    </div>
    <div class="contact contact-phone">
      <svg viewBox="0 0 10 10"><path d="M2.2 0.8 L3.8 0.8 L4.4 2.9 L3.3 3.7 Q4.2 5.8 6.3 6.7 L7.1 5.6 L9.2 6.2 L9.2 7.8 Q9.2 9.2 7.8 9.2 Q0.8 8.6 0.8 2.2 Q0.8 0.8 2.2 0.8 Z" fill="var(--text-blue)"/></svg>
      <span>Phone: 555-014-2280</span>
    </div>
    <div class="contact contact-web">
      <span>www.clearlinepipeworks.com</span>
      <span>info@clearlinepipeworks.com</span>
    </div>
  </section>

</body>
</html>
```